I want a business card design. the company is an infrastructure development company.

Target Market(s)

Government
real estate investors
real estate clients

Industry/Entity Type

Business

```html
<!DOCTYPE html>
<html lang="en">
<head>
<meta charset="utf-8">
<title>Veridan Works – Business Card</title>
<link href="https://fonts.googleapis.com/css2?family=Didact+Gothic&display=swap" rel="stylesheet">
<style>
  :root {
    --stage: #e9e6e2;
    --card: #ffffff;
    --brand-red: #e8333a;
    --brand-blue: #19a9e6;
    --blue-tint: rgba(255, 255, 255, 0.28);
    --ink-white: #ffffff;
  }
  * { margin: 0; padding: 0; box-sizing: border-box; }
  html, body {
    width: 1200px; height: 658px; overflow: hidden;
    background: var(--stage);
    font-family: "Didact Gothic", sans-serif;
  }
  .stage {
    position: relative; width: 1200px; height: 658px;
    display: flex; align-items: center; justify-content: center; gap: 60px;
  }
  .card {
    position: relative; width: 500px; height: 286px;
    background: var(--card);
    box-shadow: 0 6px 18px rgba(0, 0, 0, 0.18);
    overflow: hidden;
  }
  .wordmark {
    display: flex; align-items: center; gap: 12px;
    color: var(--brand-red);
    font-size: 38px; letter-spacing: 1px; white-space: nowrap;
  }
  .wordmark-square {
    width: 26px; height: 26px; background: var(--brand-blue); flex: none;
  }
  .card-front {
    display: flex; align-items: center; justify-content: center;
  }
  .card-back .back-top {
    height: 132px;
    display: flex; align-items: center; justify-content: center;
  }
  .card-back .wordmark { font-size: 32px; }
  .card-back .wordmark-square { width: 22px; height: 22px; }
  .back-band {
    position: absolute; left: 0; right: 0; bottom: 0; height: 154px;
    background: var(--brand-blue);
  }
  .band-motif {
    position: absolute; left: 36px; top: 12px;
    width: 130px; height: 130px; background: var(--blue-tint);
  }
  .details {
    position: absolute; right: 40px; top: 12px;
    text-align: center; color: var(--ink-white);
    font-size: 9px; line-height: 1.25;
  }
  .details h3 {
    color: var(--brand-red); font-weight: 400;
    font-size: 11px; letter-spacing: 0.5px; text-transform: uppercase;
  }
  .details .person-name { font-size: 11px; }
  .details .company-block { margin-top: 4px; }
</style>
</head>
<body>
<main class="stage">
  <section class="card card-front" aria-label="Card front">
    <div class="wordmark"><span class="wordmark-square"></span>VERIDAN WORKS</div>
  </section>

  <section class="card card-back" aria-label="Card back">
    <div class="back-top">
      <div class="wordmark"><span class="wordmark-square"></span>VERIDAN WORKS</div>
    </div>
    <div class="back-band">
      <div class="band-motif"></div>
      <div class="details">
        <div class="personal-block">
          <h3>My Details</h3>
          <p class="person-name">Tunde Adeyemi</p>
          <p>MD.</p>
          <p>+234 8010000112, +234 7010002467</p>
          <p>tunde@veridanworks.com</p>
        </div>
        <div class="company-block">
          <h3>Company Details</h3>
          <p>12, Palmgrove Close, Off Harbour Link Road,</p>
          <p>Ikeja Lagos, Nigeria</p>
          <p>+23410000006, +2347010002023</p>
          <p>info@veridanworks.com</p>
          <p>www.veridanworks.com</p>
        </div>
      </div>
    </div>
  </section>
</main>
</body>
</html>
```